Marketing Brochure design required by Video Production company

We are looking for a slick, professional and eye-catching design for a marketing brochure that will showcase our company and its services.

Purpose:
The purpose of the brochure is to show our company as experienced, capable, professional and creative.

The Brochure:
The brochure will be 10 pages (including front and back cover), designed for printing in measurements of 16cm (height) x 18cm (wide).

Attached you will find:

1. Brochure Copy/Text - this is all the text to be included in the brochure. Text in red colour is not to be included in the design but is there as a guide to assist in the design

2. Design assets - our logo and hi-resolution images to be included in the design. The filenames of the images correspond with pages in the Brochure Copy/Text (as you will see)
* this does not seem to be attaching here in ArtMarketHub. Please download this file from stashbin here: https://www.stashbin.net/s/qk4tr7wnz2lpa0e/Product_Marketing_Brochure_Assets-2016-02-07.zip?dl=0

Design:
We would like the design to be open - not cramped or squashed in. Use of space is good. We want it to look very professional, but creative. And also feel simple and easy to read.

Colours to use - blues with black & white (black & white is our brand).

Please feel free to ask any questions you might have.

Thank you.

Industry/Entity Type

It Company

Font styles to use
Sans Serif

Colors
0592cd
3176b5
3276b5
33a6d7
85cae6
cee9f5
85acd3
eaf1f7

Requirements
Must have
• As per the description.
• Download design assets from:
• https://www.stashbin.net/s/qk4tr7wnz2lpa0e/Product_Marketing_Brochure_Assets-2016-02-07.zip?dl=0

```html
<!DOCTYPE html>
<html lang="en">
<head>
<meta charset="utf-8">
<title>Brochure Spread – Services</title>
<link rel="stylesheet" href="https://fonts.googleapis.com/css2?family=Josefin+Sans:wght@300;400&display=swap">
<style>
  :root {
    --stage: #d6d6d6;
    --paper-white: #ffffff;
    --text-soft: rgba(255, 255, 255, 0.88);
    --ink-black: #0d1a26;
    --blue-deep: #3176b5;
    --blue-main: #0592cd;
    --blue-bright: #33a6d7;
    --blue-soft: #85cae6;
    --blue-mist: #85acd3;
    --blue-pale: #cee9f5;
  }
  * { box-sizing: border-box; margin: 0; padding: 0; }
  html, body { width: 1200px; height: 899px; overflow: hidden; }
  body {
    background: var(--stage);
    font-family: "Josefin Sans", sans-serif;
    color: var(--paper-white);
    position: relative;
  }
  .spread {
    position: absolute;
    left: 80px;
    top: 218px;
    width: 1040px;
    height: 462px;
    display: flex;
    box-shadow: 0 10px 30px rgba(0, 0, 0, 0.18);
  }
  .page { position: relative; width: 520px; height: 462px; overflow: hidden; }
  .page-photo { position: absolute; inset: 0; }
  .page--left .page-photo {
    background:
      radial-gradient(ellipse 60% 40% at 45% 75%, var(--blue-pale) 0%, rgba(206,233,245,0.4) 35%, transparent 70%),
      linear-gradient(200deg, var(--blue-deep) 0%, var(--blue-main) 45%, var(--ink-black) 100%);
  }
  .page--right .page-photo {
    background: linear-gradient(160deg, var(--blue-deep) 0%, var(--blue-bright) 45%, var(--blue-soft) 100%);
  }
  .section-heading {
    font-weight: 300;
    font-size: 17px;
    letter-spacing: 0.12em;
    text-transform: uppercase;
    padding-bottom: 7px;
    position: relative;
  }
  .section-heading::after {
    content: "";
    position: absolute; left: 0; bottom: 0;
    width: 48px; height: 2px;
    background: var(--paper-white);
  }
  .section-subtitle {
    font-size: 10px; font-weight: 400; margin-top: 8px; letter-spacing: 0.04em;
  }
  .section-copy {
    font-size: 9px; line-height: 1.6; font-weight: 300;
    color: var(--text-soft); margin-top: 6px;
  }
  .intro {
    position: absolute; left: 40px; top: 30px; width: 440px;
  }
  .service-list {
    position: absolute; left: 70px; top: 70px; width: 280px;
    display: flex; flex-direction: column; gap: 24px;
  }
  .gutter {
    position: absolute; left: 50%; top: 0; width: 24px; height: 100%;
    transform: translateX(-50%);
    background: linear-gradient(90deg, transparent, rgba(0,0,0,0.18) 50%, transparent);
    pointer-events: none;
  }
</style>
</head>
<body>
  <main class="spread">
    <section class="page page--left">
      <div class="page-photo" role="img" aria-label="Photo of a row of pale ceramic vases on a wooden surface"></div>
      <div class="intro">
        <h2 class="section-heading">Social Content</h2>
        <p class="section-subtitle">Short form video for social channels</p>
        <p class="section-copy">We plan, shoot and cut short clips sized for every feed, so your brand stays present, clear and easy to share across each channel and every screen your audience uses.</p>
      </div>
    </section>
    <section class="page page--right">
      <div class="page-photo" role="img" aria-label="Soft blurred photo in cool blue tones"></div>
      <div class="service-list">
        <article class="service">
          <h2 class="section-heading">Filming Only</h2>
          <p class="section-copy">Our crew arrives with camera, lights and sound, captures every shot you need and hands over the raw footage.</p>
        </article>
        <article class="service">
          <h2 class="section-heading">Editing Only</h2>
          <p class="section-copy">Send us your footage and we shape it into a clean, paced edit with titles, music and colour.</p>
        </article>
        <article class="service">
          <h2 class="section-heading">Audio Clean Up</h2>
          <p class="section-copy">We remove hum, wind and room noise, level the voices and leave a clear mix ready to publish.</p>
        </article>
      </div>
    </section>
    <div class="gutter"></div>
  </main>
</body>
</html>
```